Wohnungsbaugenossenschaft sucht Webdesign
Zielgruppe
es geht um eine Wohnungsbaugenossenschaft, die Wohnungen an unterschiedlichen Standorten vermietet. Die Webseite soll die WBG präsentieren. Einerseits sollen die Mieter über 'Laufendes' informiert werden, andereseits sollen aktuelle Mietangebote mittels externen Link für potentielle Mieter angezeigt werden.
Aufgabenstellung
Logo, siehe Dateiupload, die Seite muss aber nicht unbedingt 'grün' sein. Diverse Fotos siehe Dateiupload (müssen nicht alle verwendet werden). Texte siehe jetzige Webseite, es können auch LoremIpsum verwendet werden.
Es soll nur die Startseite gelayoutet werden.

```html
<!DOCTYPE html>
<html lang="de">
<head>
<meta charset="utf-8">
<title>Wohnungsbaugenossenschaft Lindenhof – Startseite</title>
<link rel="stylesheet" href="https://fonts.googleapis.com/css2?family=League+Spartan:wght@400;500;600;700&family=Poppins:wght@500;600&display=swap">
<style>
:root{
  --green:#13833b;
  --green-light:#3aa35a;
  --text:#222;
  --grey-bar:#e6e6e6;
  --footer:#d5d5d5;
  --head-a:#8c8f9a;
  --head-b:#b4b6c0;
  --white:#fff;
}
*{margin:0;padding:0;box-sizing:border-box}
html,body{width:1200px;height:2369px;overflow:hidden;background:var(--white)}
body{position:relative;font-family:"League Spartan",sans-serif;color:var(--text)}
.abs{position:absolute}
.topbar{left:0;top:0;width:1200px;height:37px;background:var(--grey-bar);font-size:12px;color:#666}
.topbar .hours{left:46px;top:12px}
.topbar .mail{left:630px;top:12px}
.topbar .lang{left:1090px;top:12px}
.topbar svg{position:absolute;left:1030px;top:10px}
.brand{left:22px;top:70px;display:flex;align-items:center;gap:10px;font-size:34px;font-weight:700;color:var(--green)}
.brand .mark{width:26px;height:26px;background:var(--green)}
.nav{left:298px;top:104px;display:flex;gap:28px;font-size:16px;font-weight:500;text-transform:uppercase;color:#333;letter-spacing:.3px}
.nav .active{color:var(--green)}
.stripe{left:0;top:170px;width:1200px;height:16px;background:linear-gradient(90deg,var(--green) 0 40%,var(--green-light) 40% 55%,var(--green) 55% 100%)}
.hero{left:0;top:186px;width:1200px;height:624px;background:linear-gradient(180deg,#7d7ea0 0%,#c9a6a8 30%,#8a8996 55%,#5d6068 80%,#6f8a4e 100%)}
.hero-title{left:0;width:1200px;top:463px;text-align:center;padding-left:300px;font-size:52px;font-weight:700;color:var(--white);text-shadow:0 2px 6px rgba(0,0,0,.55)}
.btn{display:flex;align-items:center;justify-content:center;background:var(--green);color:var(--white);font-family:"Poppins",sans-serif;font-weight:600}
.hero-btn{left:840px;top:612px;width:243px;height:67px;font-size:30px}
.about-img{left:28px;top:880px;width:665px;height:446px;background:linear-gradient(135deg,#dfe7ea,#9aa4ad 45%,#6b5344 60%,#e9ecee)}
.section-head{background:linear-gradient(90deg,var(--head-a),var(--head-b) 60%,var(--head-a));color:var(--white);font-size:31px;font-weight:600;letter-spacing:1px;padding-left:36px;display:flex;align-items:center}
.about-head{left:717px;top:886px;width:435px;height:57px}
.about-text{left:730px;top:962px;width:412px;font-size:18px;line-height:22px;text-align:justify}
.about-text p+p{margin-top:20px}
.about-btn{left:815px;top:1259px;width:245px;height:65px;font-size:27px}
.offers-head{left:28px;top:1426px;width:1139px;height:63px}
.offer{top:1498px;height:342px}
.offer-1{left:28px;width:372px;background:linear-gradient(180deg,#3b7bd0 0%,#c9c2ad 45%,#9c9583 90%)}
.offer-2{left:416px;width:362px;background:linear-gradient(180deg,#6e7680 0%,#e8e2dc 45%,#c6b8a6 85%,#7b8a56)}
.offer-3{left:795px;width:370px;background:linear-gradient(180deg,#7aaee0 0%,#6f757c 25%,#ecebdf 50%,#dedbc9 85%,#5f7f3c)}
.offer-text{top:1854px;font-size:17px;line-height:21px;text-align:center}
.offer-btn{top:1942px;width:175px;height:70px;font-size:29px}
.footer{left:0;top:2090px;width:1200px;height:279px;background:var(--footer);font-size:20px;color:#333}
.footer .addr{left:83px;top:32px;line-height:38px}
.footer .phones{left:83px;top:154px;line-height:40px}
.footer .phones div{display:flex;align-items:center;gap:12px}
.footer .links{left:722px;top:32px;line-height:40px}
.footer .map{left:902px;top:30px;width:266px;height:122px;background:linear-gradient(135deg,#e9eee4,#cfd8c8)}
</style>
</head>
<body>

<div class="abs topbar">
  <span class="abs hours">Sprechtage: Di 09:00 – 12:00 Uhr und Do 13:00 – 15:00</span>
  <span class="abs mail">info@wg-lindenhof.de</span>
  <svg width="16" height="16" viewBox="0 0 16 16"><path d="M2 8 L8 2 L14 8 M4 7 V14 H12 V7" fill="none" stroke="#666" stroke-width="1.5"/></svg>
  <span class="abs lang">DE | EN</span>
</div>

<div class="abs brand"><span class="mark"></span>Lindenhof</div>

<nav class="abs nav">
  <span class="active">Startseite</span>
  <span>Mietangebote</span>
  <span>Die Genossenschaft</span>
  <span>Neuigkeiten</span>
  <span>Notdienst</span>
  <span>Kontakt</span>
</nav>

<div class="abs stripe"></div>

<div class="abs hero" role="img" aria-label="Foto eines Einfamilienhauses mit Garage in der Abenddämmerung"></div>
<div class="abs hero-title">Wohnungsbaugenossenschaft</div>
<div class="abs btn hero-btn">Jetzt ansehen</div>

<div class="abs about-img" role="img" aria-label="Foto eines Händedrucks über einem Schreibtisch mit Laptop und Vertrag"></div>
<h2 class="abs section-head about-head">ÜBER UNS</h2>
<div class="abs about-text">
  <p>Wir sind seit 1926 eine eingetragene Genossenschaft und verwalten zur Zeit ca. 456 Wohneinheiten.<br>Neben Mehrfamilienhäusern verwalten wir auch Ein- und Zweifamilienhäuser.<br>Alle Wohnungsstandorte sind rund um das malerische Talstadt gelegen. Die ganze Region gehört zum wunderschönen Erzgebirge.</p>
  <p>Lassen auch Sie sich von dieser schönen Wohngegend verzaubern.</p>
</div>
<div class="abs btn about-btn">Mehr erfahren</div>

<h2 class="abs section-head offers-head">MIETANGEBOTE</h2>

<div class="abs offer offer-1" role="img" aria-label="Foto eines mehrstöckigen Altbau-Mehrfamilienhauses"></div>
<div class="abs offer offer-2" role="img" aria-label="Foto eines hellen Mehrfamilienhauses mit Gauben"></div>
<div class="abs offer offer-3" role="img" aria-label="Foto eines Wohnblocks mit grauem Dach"></div>

<p class="abs offer-text" style="left:28px;width:372px">Lorem ipsum dolor sit amet, consectetur adipisicing elit, sed do eiusmod tempor incididunt ut labore et dolore magna aliqua. Ut enim ad</p>
<p class="abs offer-text" style="left:416px;width:362px">Lorem ipsum dolor sit amet, consectetur adipisicing elit, sed do eiusmod tempor incididunt ut labore et dolore magna</p>
<p class="abs offer-text" style="left:795px;width:370px">Lorem ipsum dolor sit amet, consectetur adipisicing elit, sed do eiusmod tempor incididunt ut labore et dolore magna</p>

<div class="abs btn offer-btn" style="left:124px">Mieten</div>
<div class="abs btn offer-btn" style="left:509px">Mieten</div>
<div class="abs btn offer-btn" style="left:897px">Mieten</div>

<footer class="abs footer">
  <div class="abs addr">
    Wohnungsbaugenossenschaft Lindenhof eG Talstadt<br>
    Birkenweg 14<br>
    09123 Talstadt - Auental
  </div>
  <div class="abs phones">
    <div><svg width="16" height="16" viewBox="0 0 16 16"><path d="M3 1 L6 1 L7 5 L5 6 C6 9 7 10 10 11 L11 9 L15 10 L15 13 C15 14 14 15 13 15 C6 14 2 10 1 3 C1 2 2 1 3 1 Z" fill="none" stroke="#333" stroke-width="1.3"/></svg>(01234) 56780</div>
    <div style="padding-left:28px">(01234) 567812</div>
    <div><svg width="16" height="16" viewBox="0 0 16 16"><rect x="2" y="5" width="12" height="8" rx="1" fill="none" stroke="#333" stroke-width="1.3"/><rect x="4" y="2" width="8" height="3" fill="none" stroke="#333" stroke-width="1.3"/></svg>(01234) 567 813</div>
  </div>
  <div class="abs links">
    Kontakt<br>Impressum<br>Datenschutz<br>FAQ
  </div>
  <div class="abs map" role="img" aria-label="Kleine Anfahrtskarte mit Straßen und Standortmarkierung"></div>
</footer>

</body>
</html>
```